K7 Digital Stationery Design Project

We are looking to have stationary designs created for our company branding materials. We are looking for the following to be created.
1. Business Cards (front & back)
2. Letterhead
3. Envelopes #10
We are a new web design, development and marketing firm. Primary color scheme is desired to be blue/grey/white. This web start-up is owned and operated by individuals with 15+ years experience each in the industry so should not look as though it is a start-up by young/inexperienced individuals.
We build website & custom applications/software. In addition we provide the full spectrum of web marketing solutions including SEO, PPC, Social Media, Branding, Content Marketing and PR.
Please let us know if you have any questions. Looking forward to seeing all the amazing design ideas.
Attached is our logo.
Thanks!
Target Market(s)
Company will be nearly 100% business to business sales. Looking to work with companies that are already established, with a website, who want to take their website and/or online marketing efforts to the next level.
Industry/Entity Type
Marketing
Look and feel

```html
<!DOCTYPE html>
<html lang="en">
<head>
<meta charset="utf-8">
<title>K7 Digital — Letterhead</title>
<link rel="stylesheet" href="https://fonts.googleapis.com/css2?family=Jost:wght@300;400;600&display=swap">
<style>
  :root {
    --backdrop: #e6e7e8;
    --paper: #fefefe;
    --charcoal: #242424;
    --accent-blue: #3fa5d6;
    --mark-blue: #4a8fd0;
    --brand-grey: #8b8e92;
    --tagline-grey: #5c5f63;
  }
  * { margin: 0; padding: 0; box-sizing: border-box; }
  html, body {
    width: 933px;
    height: 1200px;
    overflow: hidden;
    background: var(--backdrop);
  }
  .letterhead {
    position: absolute;
    left: 13px;
    top: 13px;
    width: 907px;
    height: 1174px;
    background: var(--paper);
    overflow: hidden;
    font-family: "Jost", "Futura", sans-serif;
  }
  .contact-band {
    position: absolute;
    right: 0;
    top: 0;
    width: 80px;
    height: 993px;
    background: var(--charcoal);
    border-bottom-left-radius: 40px;
  }
  .contact-line {
    position: absolute;
    left: 50%;
    top: 71px;
    height: 851px;
    transform: translateX(-50%) rotate(180deg);
    writing-mode: vertical-rl;
    display: flex;
    align-items: center;
    justify-content: center;
    font-weight: 300;
    font-size: 20.5px;
    letter-spacing: 0.4px;
    color: var(--accent-blue);
    white-space: nowrap;
  }
  .contact-line .divider { margin: 12px 0; }
  .brand-block {
    position: absolute;
    right: 0;
    bottom: 0;
    width: 237px;
    height: 163px;
    background: var(--charcoal);
    border-top-left-radius: 53px;
    display: flex;
    flex-direction: column;
    align-items: center;
    justify-content: center;
    padding-top: 6px;
  }
  .brand-name {
    display: flex;
    align-items: center;
    gap: 9px;
    font-weight: 600;
    font-size: 22px;
    letter-spacing: 0.5px;
    color: var(--brand-grey);
  }
  .brand-dot {
    width: 14px;
    height: 14px;
    border-radius: 50%;
    background: var(--mark-blue);
  }
  .brand-tagline {
    margin-top: 4px;
    font-weight: 400;
    font-size: 7px;
    letter-spacing: 0.2px;
    color: var(--tagline-grey);
  }
</style>
</head>
<body>
  <main class="letterhead">
    <aside class="contact-band">
      <p class="contact-line">
        <span>2817 W. 96th Court, Lincoln, NE 68520</span>
        <span class="divider">|</span>
        <span>info@k7digital.com</span>
        <span class="divider">|</span>
        <span>www.k7digital.com</span>
      </p>
    </aside>
    <footer class="brand-block">
      <div class="brand-name"><span class="brand-dot"></span>K7 Digital</div>
      <p class="brand-tagline">Web Design, Development and Marketing</p>
    </footer>
  </main>
</body>
</html>
```